2018 Fundraiser Event Flier

We are a non profit that works in the homeless community, The Lanternwick Guild. We offer a unique program of supported employment that is all about community engagement and building relationships not only with our participants but with community businesses and non profit partners. Our mission statement is "We seek and foster partnerships between the business and nonprofit communities to respectfully and effectively guide individuals from disenfranchised communities forward in sustainable employment to realize their potential of fully enriched lives for themselves and their families" We are having a fundraising event on Dec 13 and need a flier to advertise the event both via email and physical postings. We like a black background and bright colors (see uploaded example) and want to advertise the event and a small amount about who we are. Fun and bright. We will upload two of our logos and two photos that we have used in branding previously.

```html
<!DOCTYPE html>
<html lang="en">
<head>
<meta charset="utf-8">
<title>The Lanternwick Guild – Fundraising Event Flier</title>
<link rel="stylesheet" href="https://fonts.googleapis.com/css2?family=Kalam:wght@400;700&display=swap">
<style>
  :root {
    --night: #1c1c1c;
    --night-deep: #0f0f0f;
    --plank-line: #262626;
    --lime: #8cc63f;
    --lime-bright: #a6d64a;
    --bubble-edge: #f2f2f2;
    --ink: #1a1a1a;
    --cyan: #2ec4e6;
    --paper: #ffffff;
    --skin-warm: #c98d62;
    --skin-deep: #a8704a;
    --skin-light: #e7c3a4;
    --skin-pale: #f1d9c4;
  }
  * { margin: 0; padding: 0; box-sizing: border-box; }
  html, body { width: 849px; height: 1200px; overflow: hidden; background: var(--paper); }
  .flier {
    position: relative;
    width: 849px;
    height: 1200px;
    overflow: hidden;
    background: var(--paper);
    font-family: "Kalam", cursive;
  }
  .night-panel {
    position: absolute;
    left: 0; top: 0;
    width: 849px; height: 935px;
    background:
      repeating-linear-gradient(90deg, transparent 0 118px, var(--plank-line) 118px 121px),
      linear-gradient(180deg, var(--night) 0%, var(--night-deep) 100%);
  }
  .brand-top {
    position: absolute;
    top: 34px; left: 0; width: 100%;
    text-align: center;
    color: var(--paper);
    font-weight: 700;
    font-size: 58px;
    line-height: 1;
    letter-spacing: 1px;
  }
  .brand-top .brand-mark {
    display: block;
    width: 64px; height: 64px;
    margin: 0 auto 18px;
    border-radius: 50%;
    background: var(--paper);
  }
  .accent { position: absolute; }
  .mission-bubble {
    position: absolute;
    left: 95px; top: 255px;
    width: 660px; height: 450px;
  }
  .mission-text {
    position: absolute;
    left: 165px; top: 330px;
    width: 520px;
    text-align: center;
    color: var(--ink);
    font-weight: 700;
    font-size: 24px;
    line-height: 1.36;
    text-transform: capitalize;
  }
  .hand-photo { position: absolute; }
  .hand-giving {
    left: 0; top: 712px;
    width: 400px; height: 80px;
    background: linear-gradient(90deg, var(--skin-deep) 0%, var(--skin-warm) 100%);
  }
  .hand-receiving {
    left: 480px; top: 935px;
    width: 369px; height: 80px;
    background: linear-gradient(90deg, var(--skin-pale) 0%, var(--skin-light) 100%);
  }
  .event-title {
    position: absolute;
    left: 0; top: 802px; width: 100%;
    text-align: center;
    font-weight: 700;
    font-size: 60px;
    line-height: 1.02;
    color: var(--lime-bright);
    -webkit-text-stroke: 6px var(--ink);
    paint-order: stroke fill;
  }
  .brand-bottom {
    position: absolute;
    left: 0; top: 1060px; width: 100%;
    text-align: center;
    color: var(--ink);
    font-weight: 700;
    font-size: 54px;
    line-height: 1;
  }
</style>
</head>
<body>
<main class="flier">
  <section class="night-panel">
    <header class="brand-top">
      <span class="brand-mark"></span>
      The Lanternwick Guild
    </header>

    <svg class="accent" style="left:100px;top:272px" width="56" height="56" viewBox="0 0 60 60" aria-hidden="true">
      <polygon points="0,50 50,40 22,0" fill="var(--cyan)"/>
    </svg>
    <svg class="accent" style="left:698px;top:248px" width="46" height="46" viewBox="0 0 46 46" aria-hidden="true">
      <polygon points="0,40 40,40 20,4" fill="var(--cyan)"/>
    </svg>
    <svg class="accent" style="left:770px;top:640px" width="56" height="56" viewBox="0 0 56 56" aria-hidden="true">
      <polygon points="6,0 56,28 0,52" fill="var(--cyan)"/>
    </svg>

    <svg class="mission-bubble" viewBox="0 0 660 450" aria-hidden="true">
      <path d="M40 20 H630 Q650 20 650 40 V375 Q650 395 630 395 H200 L95 445 L120 395 H40 Q20 395 20 375 V40 Q20 20 40 20 Z"
            fill="var(--lime)" stroke="var(--bubble-edge)" stroke-width="10" stroke-linejoin="round"/>
    </svg>
    <p class="mission-text">“We seek and foster partnerships between the business and nonprofit communities to respectfully &amp; effectively guide individuals from disenfranchised communities forward in sustainable employment to realize their potential of fully enriched lives for themselves and their families”</p>

    <div class="hand-photo hand-giving" role="img" aria-label="Photo of an outstretched hand reaching in from the left"></div>

    <h1 class="event-title">Fundraising Event on<br>13th December 2018</h1>
  </section>

  <div class="hand-photo hand-receiving" role="img" aria-label="Photo of an open hand reaching in from the right"></div>

  <footer class="brand-bottom">The Lanternwick Guild</footer>
</main>
</body>
</html>
```